Business cards need a revamp and change of address. I have included files of current card which has been used for 5 years. Also a photo of my new store fitout which uses a lot of colour and features inspired by cusco Peru. I would like to see design options with and without the butterfly although I do use the butterfly on my current street signage.
Updates

Reason: would like to see more designers submit

Target Market(s)

women 35 - 65

Industry/Entity Type

Business

Contact Information for Business Card

Larkvale Andean Silver Jewellery & Giftware

Requirements
Must have
• logo frontside
• backside the following text:
• Larkvale Jewellery is hand made using the highest quality 950 Peruvian Silver which is purer than 925 Sterling Silver. Larkvale's range of unique, handcrafted products are directly sourced from fair trade producer co-operatives, individual artisans and artisan groups from Peru, South America.
• Phone 02 43168272
• 7/118 Pelham Road Windsor NSW 2754
• Email : sales@larkvale.com.au
Nice to have
• Like us on face book

```html
<!DOCTYPE html>
<html lang="en">
<head>
<meta charset="utf-8">
<title>Larkvale Business Card – Front and Back</title>
<link href="https://fonts.googleapis.com/css2?family=Dosis:wght@400;500;600&display=swap" rel="stylesheet">
<style>
  :root {
    --page-bg: #e8e5e1;
    --card-bg: #000000;
    --ink: #ffffff;
    --accent-blue: #1d6fe0;
    --butterfly-deep: #0b4fb8;
    --butterfly-light: #3fa4f0;
    --photo-store-a: #2a4a66;
    --photo-store-b: #8f8a80;
    --photo-street-a: #9fb4cc;
    --photo-street-b: #c8b8a0;
  }
  * { box-sizing: border-box; margin: 0; padding: 0; }
  html, body {
    width: 1200px; height: 743px; overflow: hidden;
    background: var(--page-bg);
    font-family: "Dosis", Arial, sans-serif;
  }
  .sheet { position: relative; width: 1200px; height: 743px; }
  .card {
    position: absolute; top: 206px;
    width: 540px; height: 330px;
    background: var(--card-bg);
    color: var(--ink);
    box-shadow: 0 6px 18px rgba(0,0,0,0.25);
    overflow: hidden;
  }
  .card--front { left: 40px; }
  .card--back { left: 620px; }

  /* Front */
  .front-brand {
    position: absolute; left: 60px; top: 120px;
    font-size: 72px; font-weight: 600; line-height: 1;
    color: var(--ink);
  }
  .front-butterfly {
    position: absolute; left: 330px; top: 56px;
    width: 120px; height: 86px;
  }
  .front-url {
    position: absolute; right: 24px; bottom: 20px;
    font-size: 14px; font-weight: 400; letter-spacing: 0.5px;
  }

  /* Back */
  .back-heading {
    position: absolute; left: 30px; top: 30px;
    font-size: 32px; font-weight: 500; line-height: 1; color: var(--accent-blue);
  }
  .back-about {
    position: absolute; left: 30px; top: 76px; width: 292px;
    font-size: 11.5px; line-height: 1.32; font-weight: 500;
  }
  .back-photos {
    position: absolute; right: 18px; top: 20px;
    display: flex; gap: 12px;
  }
  .back-photo { width: 92px; height: 110px; }
  .back-photo--store { background: linear-gradient(160deg, var(--photo-store-a), var(--photo-store-b)); }
  .back-photo--street { background: linear-gradient(170deg, var(--photo-street-a), var(--photo-street-b)); }
  .back-brand {
    position: absolute; right: 40px; top: 172px;
    font-size: 38px; font-weight: 600; line-height: 1; color: var(--ink);
  }
  .contact-list {
    position: absolute; left: 30px; top: 222px;
    list-style: none;
  }
  .contact-item {
    display: flex; align-items: center; gap: 7px;
    font-size: 11px; font-weight: 500; line-height: 15px;
  }
  .contact-item--phone { font-size: 19px; line-height: 24px; margin-bottom: 5px; }
  .contact-icon { width: 12px; height: 12px; flex: none; }
  .contact-item--phone .contact-icon { width: 16px; height: 16px; }
  .social-square { width: 11px; height: 11px; background: var(--accent-blue); flex: none; }
</style>
</head>
<body>
<main class="sheet">

  <section class="card card--front" aria-label="Business card front">
    <div class="front-brand">larkvale</div>
    <svg class="front-butterfly" viewBox="0 0 120 86" role="img" aria-label="Blue morpho butterfly photograph">
      <defs>
        <radialGradient id="wing" cx="50%" cy="50%" r="60%">
          <stop offset="0%" stop-color="#3fa4f0"/>
          <stop offset="100%" stop-color="#0b4fb8"/>
        </radialGradient>
      </defs>
      <ellipse cx="60" cy="43" rx="58" ry="40" fill="url(#wing)"/>
    </svg>
    <div class="front-url">www.larkvale.com.au</div>
  </section>

  <section class="card card--back" aria-label="Business card back">
    <h1 class="back-heading">Peruvian Silver</h1>
    <p class="back-about">Larkvale Jewellery is hand made using the highest quality 950 Peruvian Silver which is purer than 925 Sterling Silver. Larkvale's range of unique, handcrafted products are directly sourced from fair trade producer co-operatives, individual artisans and artisan groups from Peru, South America.</p>

    <div class="back-photos">
      <div class="back-photo back-photo--store" role="img" aria-label="Photo of the store interior with display cabinets"></div>
      <div class="back-photo back-photo--street" role="img" aria-label="Photo of a colonial street in Cusco"></div>
    </div>

    <div class="back-brand">larkvale</div>

    <ul class="contact-list">
      <li class="contact-item contact-item--phone">
        <svg class="contact-icon" viewBox="0 0 16 16" aria-hidden="true"><path d="M4 1.5 6 4.5 4.8 6c.8 1.8 2.3 3.4 4.2 4.2L10.5 9l3 2-1 2.5C7 13.5 2.5 9 2.5 3.5Z" fill="#ffffff"/></svg>
        02 43168272
      </li>
      <li class="contact-item">
        <svg class="contact-icon" viewBox="0 0 12 12" aria-hidden="true"><circle cx="6" cy="3.5" r="2.3" fill="none" stroke="#ffffff" stroke-width="1.3"/><path d="M1.5 11.5c.5-3 2-4.2 4.5-4.2s4 1.2 4.5 4.2Z" fill="#ffffff"/></svg>
        7/118 Pelham Road Calderwood Heights NSW 2799
      </li>
      <li class="contact-item">
        <svg class="contact-icon" viewBox="0 0 12 12" aria-hidden="true"><rect x="0.8" y="2.5" width="10.4" height="7.5" fill="none" stroke="#ffffff" stroke-width="1"/><path d="M0.8 2.5 6 7l5.2-4.5" fill="none" stroke="#ffffff" stroke-width="1"/></svg>
        sales@larkvale.com.au
      </li>
      <li class="contact-item">
        <svg class="contact-icon" viewBox="0 0 12 12" aria-hidden="true"><circle cx="6" cy="6" r="5" fill="none" stroke="#ffffff" stroke-width="1.2"/><path d="M1 6h10M6 1c-2.5 3-2.5 7 0 10M6 1c2.5 3 2.5 7 0 10" fill="none" stroke="#ffffff" stroke-width="0.9"/></svg>
        www.larkvale.com.au
      </li>
      <li class="contact-item">
        <span class="social-square" aria-hidden="true"></span>
        Like us
      </li>
    </ul>
  </section>

</main>
</body>
</html>
```